Orvela Crest Advisors

Please look at the logo that we've just received and based on it provide us with the business card designs.

Industry/Entity Type

Business

Requirements
Must have
• Dummy text, so later on we can add the exact names and titles.

```html
<!DOCTYPE html>
<html lang="en">
<head>
<meta charset="UTF-8">
<title>Orvela Crest Advisors – Business Card</title>
<link href="https://fonts.googleapis.com/css2?family=Cinzel:wght@400;600&family=Roboto:wght@400&display=swap" rel="stylesheet">
<style>
  :root {
    --navy: #1a3a9c;
    --grey-text: #555a60;
    --paper: #f4f5f6;
    --stage: #e6e3de;
  }
  * { margin: 0; padding: 0; box-sizing: border-box; }
  html, body { width: 1200px; height: 800px; overflow: hidden; }
  body {
    background: var(--stage);
    display: flex;
    align-items: center;
    justify-content: center;
    gap: 40px;
  }
  .card {
    width: 540px;
    height: 309px;
    background: var(--paper);
    box-shadow: 0 6px 18px rgba(0,0,0,0.14);
    position: relative;
    overflow: hidden;
  }

  /* front */
  .brand {
    position: absolute;
    left: 34px;
    top: 68px;
    display: flex;
    align-items: center;
    gap: 12px;
    white-space: nowrap;
  }
  .brand-square { width: 24px; height: 24px; background: var(--navy); flex-shrink: 0; }
  .brand-name {
    font-family: 'Cinzel', serif;
    font-weight: 600;
    font-size: 16px;
    color: var(--navy);
    letter-spacing: 0.3px;
  }
  .rule {
    position: absolute;
    left: 72px;
    right: 30px;
    top: 100px;
    height: 1.5px;
    background: var(--navy);
  }
  .person {
    position: absolute;
    right: 34px;
    top: 36px;
    text-align: right;
    font-family: 'Cinzel', serif;
    white-space: nowrap;
  }
  .person-name { font-size: 19px; color: var(--navy); font-weight: 600; line-height: 1.1; }
  .person-title { font-size: 13px; color: var(--grey-text); letter-spacing: 1px; margin-top: 4px; }

  .contact {
    position: absolute;
    left: 72px;
    top: 132px;
    font-family: 'Roboto', sans-serif;
    font-size: 13px;
    color: var(--grey-text);
    list-style: none;
  }
  .contact li { display: flex; align-items: flex-start; gap: 14px; line-height: 18px; }
  .contact li + li { margin-top: 4px; }
  .contact svg { width: 12px; height: 12px; margin-top: 3px; flex-shrink: 0; fill: var(--navy); }
  .contact .block { margin-bottom: 6px; }

  /* back */
  .card-back {
    display: flex;
    align-items: center;
    justify-content: center;
    gap: 14px;
    white-space: nowrap;
  }
  .card-back .brand-square { width: 32px; height: 32px; }
  .card-back .brand-name { font-size: 24px; }
</style>
</head>
<body>

<section class="card card-front" aria-label="Business card front">
  <div class="brand">
    <span class="brand-square"></span>
    <span class="brand-name">Orvela Crest Advisors</span>
  </div>
  <div class="person">
    <div class="person-name">ADRIAN VELL</div>
    <div class="person-title">CEO/FOUNDER</div>
  </div>
  <div class="rule"></div>

  <ul class="contact">
    <li class="block">
      <svg viewBox="0 0 12 12"><path d="M6 0a4 4 0 0 0-4 4c0 3 4 8 4 8s4-5 4-8a4 4 0 0 0-4-4zm0 5.6A1.6 1.6 0 1 1 6 2.4a1.6 1.6 0 0 1 0 3.2z"/></svg>
      <span>4210 Birchwood Court<br>Fairbanks, Alaska 36812</span>
    </li>
    <li>
      <svg viewBox="0 0 12 12"><path d="M2.4 0.6l2 2-1 1.4a7 7 0 0 0 4.6 4.6l1.4-1 2 2-1.4 1.8C5 11 1 7 0.6 2z"/></svg>
      <span>614 208 3371</span>
    </li>
    <li>
      <svg viewBox="0 0 12 12"><path d="M3 0h6v12H3zm1 1.5v7.5h4V1.5zM5.3 10h1.4v1H5.3z"/></svg>
      <span>752 390 1846</span>
    </li>
    <li>
      <svg viewBox="0 0 12 12"><path d="M3 0h6v3H3zM1 4h10v6H9v2H3v-2H1zm3 4v3h4V8z"/></svg>
      <span>519 674 2083</span>
    </li>
    <li>
      <svg viewBox="0 0 12 12"><path d="M0 2h12v8H0zm1 1v.4l5 3.2 5-3.2V3zm0 1.6V9h10V4.6L6 7.8z"/></svg>
      <span>hello@orvelacrest.com</span>
    </li>
    <li>
      <svg viewBox="0 0 12 12"><circle cx="6" cy="6" r="6"/><path d="M0 6h12M6 0c-3 3-3 9 0 12M6 0c3 3 3 9 0 12" stroke="#f4f5f6" stroke-width="0.8" fill="none"/></svg>
      <span>www.orvelacrest.com</span>
    </li>
  </ul>
</section>

<section class="card card-back" aria-label="Business card back">
  <span class="brand-square"></span>
  <span class="brand-name">Orvela Crest Advisors</span>
</section>

</body>
</html>
```